Construction company focused on concrete and shed construction.

We need to update our current business card for ridgeforgebuilds.com.au we would like an eye catching design with blue, grey and white incorporating our current logo.
Our company started off in concreting and due to varying factors we have expanded to include shed construction as well.
This has led to our current Logo looking a little out of place and somehow need to use the card to bring in the shed construction side of the business while not having to change current concrete look "KESTRO" logo as we already have this incorporated into our company clothing and are not willing to change this yet.
Photo image attached for inspiration/ visual reference of type of work, not to be used on final design.
Please no cheesy designs of men in hard hats and tools
Final design should demonstrate a modern and service focused company.

Target Market(s)

Farmers, Business owners, Developers, Architects, Commercial project delivery

Industry/Entity Type

Construction Company

Contact Information for Business Card

Kestro Constructions.
7b Harlow st
South Launceston Tas
03 62918873

Font styles to use
Other font styles liked:
• see font in logo

Colors
3176b5
b2b2b2

Requirements
Must have
• Easy to read font,
• good contrast between back ground and writing
Nice to have
• Modern and corporate look with a fun but professional image.
Should not have
• Comic images or shadow images of tools/ people.

```html
<!DOCTYPE html>
<html lang="en">
<head>
<meta charset="utf-8">
<title>Kestro Constructions – Business Card</title>
<link rel="stylesheet" href="https://fonts.googleapis.com/css2?family=Saira+Semi+Condensed:wght@600;700&family=Roboto:wght@400&display=swap">
<style>
  :root {
    --brand-blue: #1f64ab;
    --brand-grey: #4a5157;
    --ink: #1d1d1f;
    --card-white: #f7f7f5;
    --backdrop: #e9e9e9;
    --site-light: #eef0f0;
    --site-mid: #d9dcdc;
  }
  * { margin: 0; padding: 0; box-sizing: border-box; }
  html, body {
    width: 1200px;
    height: 1200px;
    overflow: hidden;
    background: var(--backdrop);
  }
  .canvas {
    position: relative;
    width: 1200px;
    height: 1200px;
  }
  .card {
    position: absolute;
    width: 712px;
    height: 418px;
    background: var(--card-white);
    overflow: hidden;
  }
  .card--front { left: 238px; top: 118px; }
  .card--back  { left: 230px; top: 644px; }

  .site-photo {
    position: absolute;
    inset: 0;
    background: linear-gradient(180deg, var(--site-mid) 0%, var(--site-light) 45%, #f5f6f6 100%);
  }

  .brand-mark {
    position: absolute;
    display: flex;
    align-items: center;
    gap: 12px;
    white-space: nowrap;
  }
  .brand-mark__dot {
    border-radius: 50%;
    background: var(--brand-blue);
    flex: none;
  }
  .brand-mark__name {
    font-family: "Saira Semi Condensed", sans-serif;
    font-weight: 700;
    color: var(--brand-grey);
    letter-spacing: 1px;
    line-height: 1;
  }
  .card--front .brand-mark { left: 0; right: 0; top: 150px; justify-content: center; }
  .card--front .brand-mark__dot { width: 44px; height: 44px; }
  .card--front .brand-mark__name { font-size: 62px; }

  .card--back .brand-mark { left: 390px; top: 170px; }
  .card--back .brand-mark__dot { width: 44px; height: 44px; }
  .card--back .brand-mark__name { font-size: 58px; }

  .person {
    position: absolute;
    left: 36px;
    top: 30px;
  }
  .person__name {
    font-family: "Saira Semi Condensed", sans-serif;
    font-weight: 600;
    font-size: 30px;
    color: var(--brand-blue);
    line-height: 1.1;
  }
  .person__role {
    font-family: "Roboto", sans-serif;
    font-size: 16px;
    color: var(--ink);
    margin-top: 4px;
  }

  .contact {
    position: absolute;
    left: 36px;
    top: 246px;
    font-family: "Roboto", sans-serif;
    font-size: 18px;
    color: var(--ink);
  }
  .contact__company {
    font-family: "Saira Semi Condensed", sans-serif;
    font-weight: 700;
    font-size: 23px;
    color: var(--brand-blue);
    letter-spacing: 0.3px;
    margin-bottom: 6px;
  }
  .contact__row {
    display: flex;
    align-items: center;
    gap: 10px;
    height: 25px;
  }
  .contact__row svg { width: 18px; height: 18px; fill: var(--brand-blue); flex: none; }
  .contact__address { margin-top: 5px; }
</style>
</head>
<body>
<main class="canvas">

  <section class="card card--front" aria-label="Card front">
    <div class="site-photo" role="img" aria-label="Faded photograph of a freshly poured concrete slab on a shed construction site"></div>
    <div class="brand-mark">
      <span class="brand-mark__dot"></span>
      <span class="brand-mark__name">KESTRO</span>
    </div>
  </section>

  <section class="card card--back" aria-label="Card back">
    <div class="person">
      <h1 class="person__name">Employee Name</h1>
      <p class="person__role">Managing Director</p>
    </div>

    <div class="contact">
      <h2 class="contact__company">KESTRO CONSTRUCTIONS</h2>
      <p class="contact__row">
        <svg viewBox="0 0 24 24" aria-hidden="true"><path d="M3 9c0-3 4-5 9-5s9 2 9 5v2h-5V8.5c-1-.5-2.5-.8-4-.8s-3 .3-4 .8V11H3z M6 12h12l2 8H4z"/></svg>
        <span>03 62918873</span>
      </p>
      <p class="contact__row">
        <svg viewBox="0 0 24 24" aria-hidden="true"><path d="M2 5h20v14H2z M4 7l8 6 8-6v-.5H4z" fill-rule="evenodd"/></svg>
        <span>name@ridgeforgebuilds.com</span>
      </p>
      <p class="contact__row">
        <svg viewBox="0 0 24 24" aria-hidden="true"><path d="M12 2a10 10 0 1 0 0 20 10 10 0 0 0 0-20zm0 2c1.2 1.4 2 3.6 2.2 7H9.8C10 7.6 10.8 5.4 12 4zm-2.2 9h4.4c-.2 3.4-1 5.6-2.2 7-1.2-1.4-2-3.6-2.2-7zM4.1 11a8 8 0 0 1 4.2-6.1C7.6 6.6 7.9 8.6 7.8 11zm0 2h3.7c.1 2.4-.2 4.4-.5 6.1A8 8 0 0 1 4.1 13zm12.1-2c-.1-2.4-.4-4.4-.5-6.1a8 8 0 0 1 4.2 6.1zm0 2h3.7a8 8 0 0 1-4.2 6.1c.3-1.7.6-3.7.5-6.1z"/></svg>
        <span>www.ridgeforgebuilds.com</span>
      </p>
      <p class="contact__address">7B Harlow St South Launceston TAS</p>
    </div>

    <div class="brand-mark">
      <span class="brand-mark__dot"></span>
      <span class="brand-mark__name">KESTRO</span>
    </div>
  </section>

</main>
</body>
</html>
```